Detail Shop Business card design

i need a business card design for my new detailing company called 'Brenner's Detail Shop'. i want an all black and white design . simple, direct and to the point. i want the designer to choose a fitting font to match the logothe front should have logo, address, phone and email and the back side should have a slogan and text indicating that we offer services on anything including cars, trucks, motorcycles and RVs. slogan will read "we take pride in your ride"
maybe also very small on the back side the IG icon with Brenners_Detail_Shop

phone 482.615.7734
address 7384 E Harlow Ave
Spokane WA 99342
email: BrennersDetail@quorvail.com

Target Market(s)

all ages , auto enthusiasts

Industry/Entity Type

Automotive

Contact Information for Business Card

the front should have logo, address, phone and email and the back side should have a slogan and text indicating that we offer services on anything including cars, trucks, motorcycles and RVs. slogan will read "we take pride in your ride"

phone 482.615.7734
address 7384 E Harlow Ave
Spokane WA 99342

Colors
000000
ffffff

Requirements
Must have
• bold font and very simple design with good spacing
Nice to have
• anything creative from the designer indicating we service any types of vehicles
Should not have
• any colors ,

```html
<!DOCTYPE html>
<html lang="en">
<head>
<meta charset="utf-8">
<title>Brenner's Detail Shop – Business Card</title>
<link rel="stylesheet" href="https://fonts.googleapis.com/css2?family=Lato:wght@400;700;900&family=Alfa+Slab+One&display=swap">
<style>
  :root {
    --ink: #000000;
    --paper: #ffffff;
    --stage: #2a2a2c;
    --muted: #cfcfcf;
  }
  * { box-sizing: border-box; margin: 0; padding: 0; }
  html, body { width: 1200px; height: 800px; overflow: hidden; }
  body {
    background: var(--stage);
    font-family: "Lato", Arial, sans-serif;
    display: flex;
    align-items: center;
    justify-content: center;
    gap: 40px;
  }
  .card {
    position: relative;
    width: 540px;
    height: 310px;
    overflow: hidden;
  }
  .card--back { background: var(--ink); color: var(--paper); }
  .card--front { background: var(--paper); color: var(--ink); }
  .card__bands {
    position: absolute;
    inset: 0;
    width: 100%;
    height: 100%;
  }
  .brand {
    position: absolute;
    top: 58px;
    left: 0;
    right: 0;
    display: flex;
    align-items: center;
    justify-content: center;
    gap: 12px;
  }
  .brand__dot {
    width: 22px;
    height: 22px;
    border-radius: 50%;
    background: currentColor;
  }
  .brand__name {
    font-family: "Alfa Slab One", Georgia, serif;
    font-size: 30px;
    font-weight: 400;
    letter-spacing: 0.5px;
  }
  .slogan {
    position: absolute;
    top: 128px;
    left: 0;
    right: 0;
    text-align: center;
    font-size: 15px;
    font-weight: 700;
    letter-spacing: 4px;
  }
  .contact {
    position: absolute;
    top: 128px;
    left: 0;
    right: 0;
    display: flex;
    justify-content: center;
    align-items: center;
    gap: 14px;
    font-size: 14px;
    line-height: 1.4;
  }
  .contact__address { text-align: right; }
  .contact__divider {
    width: 1.5px;
    height: 38px;
    background: var(--ink);
  }
  .contact__line {
    display: flex;
    align-items: center;
    gap: 6px;
  }
  .contact__icon { width: 11px; height: 11px; }
</style>
</head>
<body>

  <section class="card card--back" aria-label="Card back">
    <svg class="card__bands" viewBox="0 0 540 310" aria-hidden="true">
      <rect x="0" y="176" width="540" height="6" fill="#ffffff"/>
      <rect x="257" y="166" width="26" height="26" fill="#000000" stroke="#ffffff" stroke-width="2"/>
      <polygon points="270,172 272,177 277,177 273,180 275,185 270,182 265,185 267,180 263,177 268,177" fill="#ffffff"/>
      <polygon points="0,256 540,256 540,290 0,290 14,273" fill="#ffffff"/>
    </svg>
    <div class="brand">
      <span class="brand__dot"></span>
      <span class="brand__name">Brenner's Detail Shop</span>
    </div>
    <p class="slogan">we take pride in your ride</p>
  </section>

  <section class="card card--front" aria-label="Card front">
    <svg class="card__bands" viewBox="0 0 540 310" aria-hidden="true">
      <rect x="0" y="196" width="540" height="14" fill="#000000"/>
      <rect x="256" y="190" width="28" height="26" fill="#ffffff" stroke="#000000" stroke-width="2"/>
      <polygon points="270,196 272,201 277,201 273,204 275,209 270,206 265,209 267,204 263,201 268,201" fill="#000000"/>
      <polygon points="0,262 540,262 540,294 0,294 14,278" fill="#000000"/>
    </svg>
    <div class="brand">
      <span class="brand__dot"></span>
      <span class="brand__name">Brenner's Detail Shop</span>
    </div>
    <div class="contact">
      <address class="contact__address" style="font-style: normal;">
        7384 E Harlow Ave<br>Spokane WA 99342
      </address>
      <span class="contact__divider"></span>
      <div>
        <p class="contact__line">
          <svg class="contact__icon" viewBox="0 0 12 12" aria-hidden="true"><rect x="1" y="1" width="10" height="10" fill="none" stroke="#000" stroke-width="1.5"/></svg>
          482.615.7734
        </p>
        <p class="contact__line">
          <svg class="contact__icon" viewBox="0 0 12 12" aria-hidden="true"><rect x="0" y="2" width="12" height="8" fill="#000"/><polyline points="0,2 6,7 12,2" fill="none" stroke="#fff" stroke-width="1.2"/></svg>
          BrennersDetail@quorvail.com
        </p>
      </div>
    </div>
  </section>

</body>
</html>
```